Poster to advertise velquin and dermal fillers

I want a poster to put up in beauty salons to advertise velquin and dermal fillers.
Velquin is used to reduce fine lines and wrinkles around the eyes and across the forehead, between the eyebrows and dermal fillers are used to add volume under the skin where it begins to sag.
The products are mainly used by women.
I am an advanced aesthetic nurse and a member of the Harwell Guild of cosmetic nurses.
I want the poster to be quite feminine with soft colours, eye catching and not too busy, not too much information. It may go in the window of the salon to attract passing trade.
I want it to state that these treatments are available at the particular salon by an advanced trained nurse. "Please ask for further details or to arrange a consultation". etc
My company is called plum Willow

Target Market(s)

Mainly women

Industry/Entity Type

Nurse

Requirements
Should not have
• harsh colours, no jokes

```html
<!DOCTYPE html>
<html lang="en">
<head>
<meta charset="utf-8">
<title>Plum Willow – Velquin &amp; Dermal Fillers</title>
<link href="https://fonts.googleapis.com/css2?family=Cinzel:wght@400;700&family=Open+Sans:ital,wght@1,400&display=swap" rel="stylesheet">
<style>
  :root {
    --cream: #e9e8a9;
    --cream-light: #efecb2;
    --band-top: #d2a57a;
    --band-olive: #d9d99b;
    --rule: #b99a72;
    --tan: #c9a272;
    --tan-deep: #a3845b;
    --tan-pale: #d9c48f;
    --olive-text: #7c7a55;
    --olive-green: #6f7a4f;
    --gold: #c9b472;
    --gold-dark: #a8924f;
    --skin: #e2b9a0;
    --skin-shadow: #b98a72;
    --guild: #8a2c22;
  }
  html, body {
    margin: 0;
    padding: 0;
    overflow: hidden;
    background: #ffffff;
  }
  .poster {
    position: relative;
    width: 900px;
    height: 1200px;
    overflow: hidden;
    background: var(--cream);
    font-family: "Cinzel", serif;
  }
  .poster-art {
    position: absolute;
    inset: 0;
  }
  .brand-name {
    position: absolute;
    left: 0;
    width: 804px;
    top: 138px;
    margin: 0;
    text-align: center;
    font-weight: 700;
    font-size: 100px;
    line-height: 1;
    letter-spacing: 2px;
    color: var(--tan);
  }
  .treatments {
    position: absolute;
    right: 120px;
    top: 242px;
    margin: 0;
    font-weight: 700;
    font-size: 37px;
    letter-spacing: 2px;
    color: var(--tan);
  }
  .availability {
    position: absolute;
    right: 122px;
    top: 302px;
    margin: 0;
    font-family: "Open Sans", sans-serif;
    font-style: italic;
    font-size: 66px;
    line-height: 1;
    color: var(--tan-deep);
  }
  .question {
    position: absolute;
    left: 0;
    width: 804px;
    top: 408px;
    margin: 0;
    text-align: center;
    font-weight: 700;
    font-style: italic;
    font-size: 56px;
    line-height: 73px;
    letter-spacing: 2px;
    color: var(--tan-pale);
  }
  .consultation {
    position: absolute;
    left: 16px;
    top: 836px;
    margin: 0;
    font-weight: 700;
    font-size: 35px;
    line-height: 46px;
    letter-spacing: 1px;
    color: var(--olive-text);
  }
  .credentials {
    position: absolute;
    left: 174px;
    top: 1062px;
    margin: 0;
    font-weight: 700;
    font-size: 27px;
    line-height: 32px;
    letter-spacing: 1px;
    color: var(--olive-green);
  }
  .guild {
    position: absolute;
    left: 12px;
    top: 1162px;
    display: flex;
    align-items: center;
    gap: 8px;
  }
  .guild-square {
    width: 22px;
    height: 22px;
    background: var(--guild);
  }
  .guild-name {
    width: 200px;
    font-weight: 700;
    font-size: 14px;
    line-height: 17px;
    color: var(--guild);
  }
</style>
</head>
<body>
<main class="poster">
  <svg class="poster-art" width="900" height="1200" viewBox="0 0 900 1200" aria-hidden="true">
    <defs>
      <linearGradient id="goldSweep" x1="0" y1="0" x2="0" y2="1">
        <stop offset="0" stop-color="#ddd08f"/>
        <stop offset="0.5" stop-color="var(--gold)"/>
        <stop offset="1" stop-color="var(--gold-dark)"/>
      </linearGradient>
      <linearGradient id="panelShade" x1="0" y1="0" x2="0" y2="1">
        <stop offset="0" stop-color="var(--cream-light)"/>
        <stop offset="1" stop-color="#e6e3a6"/>
      </linearGradient>
    </defs>
    <rect class="top-band" x="0" y="0" width="900" height="8" fill="var(--band-top)"/>
    <rect class="olive-band" x="0" y="8" width="900" height="100" fill="var(--band-olive)"/>
    <path class="lower-sweep" d="M0 690 C200 640 480 630 600 660 L900 720 V1200 H0 Z" fill="url(#goldSweep)"/>
    <path class="cream-stripe" d="M0 670 C220 640 470 640 560 668 L560 690 C460 668 220 670 0 705 Z" fill="#f4efc8"/>
    <path class="cream-stripe-thin" d="M0 735 C220 705 450 705 540 728 L540 738 C450 720 220 722 0 750 Z" fill="#efe6b8" opacity="0.8"/>
    <path class="dark-ring" d="M-180 990 A560 170 0 0 0 940 990" fill="none" stroke="#3e3a28" stroke-width="10" opacity="0.75"/>
    <path class="light-ring" d="M-150 990 A530 150 0 0 0 910 990" fill="none" stroke="#f1e9c2" stroke-width="6" opacity="0.8"/>
    <path class="page-panel" d="M0 110 H804 V690 C720 660 600 650 520 672 C360 640 160 650 0 680 Z" fill="url(#panelShade)" stroke="#c8c08a" stroke-width="1.5"/>
    <line class="panel-rule" x1="0" y1="389" x2="804" y2="389" stroke="var(--rule)" stroke-width="3"/>
    <path class="portrait" role="img" aria-label="Portrait of a young woman with smooth skin, framed by the peeled page"
      d="M525 668 C620 640 780 660 900 745 V1200 H575 C548 1080 530 880 525 668 Z" fill="var(--skin)"/>
    <path class="portrait-shade" d="M525 668 C620 640 780 660 900 745 V800 C780 730 640 690 540 700 Z" fill="var(--skin-shadow)" opacity="0.55"/>
  </svg>

  <h1 class="brand-name">PLUM WILLOW</h1>
  <p class="treatments">VELQUIN &amp; DERMAL FILLERS</p>
  <p class="availability">AVAILABLE HERE</p>
  <p class="question">WANTING A MORE<br>YOUTHFUL<br>APPEARANCE?</p>
  <p class="consultation">FOR FURTHER<br>INFORMATION BOOK<br>A FREE CONSULTATION<br>HERE</p>
  <p class="credentials">NURSE TRAINED IN ADVANCED<br>AESTHETIC PROCEDURES</p>
  <div class="guild">
    <span class="guild-square"></span>
    <span class="guild-name">Harwell Guild of Cosmetic Nurses</span>
  </div>
</main>
</body>
</html>
```